label design for coffee bean packaging

Logo will be provided. Label design for package of coffee beans for a micro roasted coffee company. Need to have space to write in origin, weight with check box for 1/4, 1/2, 1lb. Need to have check boxes for Light, Medium, Dark. Creative unique label design with boarders and fun, modern design. Company name is Cedar Brook Roasting Company. See attached logo. I have source files for logo if needed for design.
Industry/Entity Type
Coffee Shop
Font styles to use
Other font styles liked:
- Montez, kautiva cyrillic, uniform bold
Colors
f78f20
faa54b
f37122
fece3e
acd036
Requirements
Must have
- logo included in the design

```html
<!DOCTYPE html>
<html lang="en">
<head>
<meta charset="utf-8">
<title>Cedar Brook Roasting Company – Coffee Bag Label</title>
<link rel="stylesheet" href="https://fonts.googleapis.com/css2?family=Oswald:wght@400;500;600&display=swap">
<style>
  :root {
    --page-bg: #e4e7e8;
    --label-brown: #4a2814;
    --label-brown-deep: #3d200f;
    --frame-gold: #fece3e;
    --frame-orange: #f78f20;
    --leaf-green: #acd036;
    --leaf-orange: #f37122;
    --card-tan: #e2c08f;
    --rule-brown: #8a6138;
    --ink: #3a2212;
    --badge-white: #ffffff;
  }
  * { box-sizing: border-box; margin: 0; padding: 0; }
  html, body { width: 1200px; height: 901px; overflow: hidden; }
  body {
    background: var(--page-bg);
    font-family: "Oswald", "Arial Narrow", sans-serif;
    color: var(--ink);
    position: relative;
  }
  .label {
    position: absolute;
    left: 297px; top: 70px;
    width: 606px; height: 760px;
    background: var(--label-brown);
    overflow: hidden;
  }
  .label__botanical {
    position: absolute; inset: 0;
    background:
      radial-gradient(ellipse 38% 30% at 18% 22%, rgba(172,208,54,.38), transparent 70%),
      radial-gradient(ellipse 40% 32% at 85% 18%, rgba(243,113,34,.42), transparent 70%),
      radial-gradient(ellipse 34% 26% at 12% 60%, rgba(243,113,34,.36), transparent 70%),
      radial-gradient(ellipse 34% 28% at 86% 52%, rgba(172,208,54,.36), transparent 70%),
      linear-gradient(180deg, var(--label-brown) 0%, var(--label-brown-deep) 100%);
  }
  .label__frame {
    position: absolute;
    left: 22px; top: 22px; right: 22px; bottom: 22px;
    border: 3px solid var(--frame-gold);
    box-shadow: inset 0 0 0 1px var(--frame-orange);
  }
  .badge {
    position: absolute;
    left: 154px; top: 118px;
    width: 276px; height: 276px;
    border-radius: 50%;
    background: var(--badge-white);
    display: flex; align-items: center; justify-content: center;
    text-align: center;
    padding: 0 34px;
  }
  .badge__name {
    font-weight: 500;
    font-size: 34px;
    line-height: 1.15;
    text-transform: uppercase;
    letter-spacing: 1px;
    color: var(--label-brown);
  }
  .order-card {
    position: absolute;
    left: 47px; top: 453px;
    width: 506px;
    background: var(--card-tan);
  }
  .order-card__row {
    display: grid;
    border-bottom: 2px solid var(--rule-brown);
  }
  .order-card__row:last-child { border-bottom: none; }
  .order-card__cell {
    display: flex; align-items: center;
    padding: 0 12px;
    font-size: 22px;
    border-right: 2px solid var(--rule-brown);
  }
  .order-card__cell:last-child { border-right: none; }
  .row--origin { grid-template-columns: 170px 1fr; height: 63px; }
  .row--origin .order-card__cell:first-child { font-size: 30px; font-weight: 500; }
  .row--roast, .row--weight { grid-template-columns: 106px 69px 116px 61px 81px 1fr; }
  .row--roast { height: 55px; }
  .row--weight { height: 47px; }
  .row--weight .order-card__cell:nth-child(odd) { justify-content: center; }
  .row--date { grid-template-columns: 170px 1fr; height: 51px; }
  .row--web {
    height: 43px; grid-template-columns: 1fr;
  }
  .row--web .order-card__cell {
    justify-content: center;
    font-size: 15px; font-weight: 600;
    letter-spacing: 2.2px;
  }
</style>
</head>
<body>
  <main class="label">
    <div class="label__botanical" role="img" aria-label="Engraved coffee branches with leaves and cherries in green and orange on dark brown"></div>
    <div class="label__frame"></div>

    <div class="badge">
      <span class="badge__name">Cedar Brook Roasting Company</span>
    </div>

    <section class="order-card">
      <div class="order-card__row row--origin">
        <div class="order-card__cell">ORIGIN</div>
        <div class="order-card__cell"></div>
      </div>
      <div class="order-card__row row--roast">
        <div class="order-card__cell">LIGHT</div>
        <div class="order-card__cell"></div>
        <div class="order-card__cell">MEDIUM</div>
        <div class="order-card__cell"></div>
        <div class="order-card__cell">DARK</div>
        <div class="order-card__cell"></div>
      </div>
      <div class="order-card__row row--weight">
        <div class="order-card__cell">1/4</div>
        <div class="order-card__cell"></div>
        <div class="order-card__cell">1/2</div>
        <div class="order-card__cell"></div>
        <div class="order-card__cell">1lb</div>
        <div class="order-card__cell"></div>
      </div>
      <div class="order-card__row row--date">
        <div class="order-card__cell">Date Roasted</div>
        <div class="order-card__cell"></div>
      </div>
      <div class="order-card__row row--web">
        <div class="order-card__cell">www.cedarbrookroastingcompany.com</div>
      </div>
    </section>
  </main>
</body>
</html>
```